Toy Company Needs a Web Site For a New Toy

We need a web site for a new toy called "Zippa Loop Trike". The bike is a plastic, non motorized ride on toy for kids ages 1.5 - 5 years of age. The bike is being launched in three colors, red, blue and pink, though we may include a black option too.

For the web site we want something bold and colorful that communicates fun, therefore NO dull colors like black or grey. Nothing too cluttered. We want the site to attract the attention of kids but also give the parents a sense of confidence in our professionalism as a trustworthy toy company. The home page should focus on the bike, with different views of the bike and a small write-up on some of its key features. We would also like the home page to have a video of the bike in play. A obvious link to the shopping basket must be present as well. The site must include a shopping basket and ordering system.

Attached is a screenshot of a site that has the colourfulness and playfulness that we are looking for. Please have a look.

The bike images attached are renderings from the CAD software, actual high res photos will be used when the site is developed.

The product logo is attached and MUST be used on the site. It must be BOLD and can be incorporated into the actual website design.

The site pages are:
Home
Gallery
Buy
Contact

Competitors:
www.brambleplay.example
www.quorvaride.example
I do not like either of their sites.

We only have one product at this time, so the site is to be focused on that product, not a whole catalog of products. It is really a single product with the ability to purchase.
Updates

Project Deadline Extended
Reason: I am extending this competition in order to give me more time to review each design and provide the feedback that the designers deserve.

Target Market(s)

Parents, children ages 1.5 - 5.

Industry/Entity Type

It Company

Colors
0555a3
eb1f27
9bcb3c
faed22
f78f20
f37022
e34197
a6459a
6b449b

Requirements
Must have
• Please use the logo attached, but feel free to use different colors.
Should not have
• Dull colors like black and grey

```html
<!DOCTYPE html>
<html lang="en">
<head>
<meta charset="utf-8">
<title>Zippa Loop Trike</title>
<link href="https://fonts.googleapis.com/css2?family=Ultra&family=Shadows+Into+Light&family=Arimo:wght@400;700&display=swap" rel="stylesheet">
<style>
:root{
  --deep:#0a5e78;
  --deep-dark:#004a60;
  --sky:#2ea3d8;
  --sky-light:#4fb8e6;
  --pale:#eaf4f8;
  --red:#e8202a;
  --white:#ffffff;
  --nav-bg:#eef5f8;
  --ink:#555555;
  --muted:#8a8a8a;
  --heading-grey:#8d8d8d;
  --cream:#fbf5dc;
}
*{margin:0;padding:0;box-sizing:border-box}
html,body{width:1200px;height:1036px;overflow:hidden}
body{position:relative;background:var(--pale);font-family:"Arimo",Arial,sans-serif;color:var(--ink)}
.abs{position:absolute}
.band-top{left:0;top:0;width:1200px;height:93px;background:linear-gradient(180deg,#0a8fc0 0%,var(--deep) 100%)}
.band-hero{left:0;top:93px;width:1200px;height:461px;background:radial-gradient(ellipse at 30% 40%,var(--sky-light) 0%,var(--sky) 55%,#1e8fc8 100%)}
.band-foot{left:0;top:919px;width:1200px;height:117px;background:var(--deep-dark)}

.brand-badge{left:208px;top:9px;width:180px;height:180px;border-radius:50%;background:var(--red);border:6px solid var(--white);display:flex;align-items:center;justify-content:center;text-align:center;z-index:3;box-shadow:0 2px 6px rgba(0,0,0,.25)}
.brand-badge span{font-family:"Ultra",serif;color:var(--white);font-size:20px;line-height:1.15;width:130px}

.nav-bar{left:368px;top:93px;width:616px;height:72px;background:var(--nav-bg);border-radius:0 0 8px 0}
.nav-link{top:122px;font-family:"Ultra",serif;font-size:12px;color:#666;letter-spacing:.3px}
.nav-link.is-active{color:var(--red)}
.nav-sep{top:121px;width:1px;height:18px;background:#aab6bc}

.order-btn{left:866px;top:48px;width:117px;height:30px;border-radius:6px;background:var(--red);color:var(--white);font-family:"Ultra",serif;font-size:12px;display:flex;align-items:center;justify-content:center;letter-spacing:.4px}

.cart-title{left:870px;top:100px;font-family:"Shadows Into Light",cursive;font-size:24px;color:#222}
.cart-count{left:878px;top:134px;display:flex;align-items:center;gap:6px;font-family:"Shadows Into Light",cursive;font-size:20px;color:var(--sky)}

.hero-title{left:209px;top:241px;font-family:"Ultra",serif;font-size:23px;color:var(--white);text-shadow:2px 2px 2px rgba(0,0,0,.35)}
.hero-copy{left:209px;top:298px;width:346px;font-family:"Shadows Into Light",cursive;font-size:20px;line-height:29px;color:var(--white);text-align:justify}
.buy-btn{left:209px;top:445px;width:108px;height:35px;background:var(--white);box-shadow:2px 3px 3px rgba(0,0,0,.3);display:flex;align-items:center;justify-content:center;gap:5px;font-family:"Ultra",serif;font-size:12px;color:var(--red)}

.hero-photo{left:584px;top:213px;width:399px;height:265px;border:6px solid var(--cream);background:linear-gradient(180deg,#4c7a33 0%,#6e9a45 45%,#5b5f5f 75%,#3d4243 100%)}

.content-card{left:208px;top:508px;width:775px;height:494px;background:var(--white);border-radius:7px;box-shadow:0 4px 10px rgba(0,0,0,.15)}
.section-title{font-family:"Ultra",serif;font-size:11.5px;letter-spacing:.2px}
.section-title.is-red{color:var(--red)}
.section-title.is-grey{color:var(--heading-grey)}
.body-copy{font-size:9.3px;line-height:11px;color:var(--muted)}
.feature-thumb{left:244px;top:657px;width:127px;height:95px;background:linear-gradient(180deg,#5e8a40 0%,#3b56b4 50%,#6d8a55 100%)}
.card-divider{left:701px;top:537px;width:1px;height:321px;background:#e2e2e2}

.signup-field{left:718px;top:594px;width:156px;height:29px;background:#f1f1f1;font-size:8px;color:#aaa;padding:10px 0 0 13px}
.signup-btn{left:874px;top:594px;width:60px;height:29px;background:var(--red);display:flex;align-items:center;justify-content:center}

.share-row{left:718px;top:702px;display:flex;gap:6px;align-items:center}
.share-btn{display:flex;align-items:center;gap:3px;height:14px;border:1px solid #c8d0d8;border-radius:2px;padding:0 4px;font-size:8px;font-weight:700;color:#3b5a8a;background:#f4f7fb}
.share-btn i{display:block;width:7px;height:7px;background:#4a6aa8}
.share-btn.is-hot{background:#e8533c;border-color:#e8533c;color:var(--white)}
.share-btn.is-hot i{background:var(--white)}
.share-count{height:14px;border:1px solid #ccc;border-radius:2px;padding:0 3px;font-size:7.5px;line-height:12px;color:#444}

.follow-rule{left:718px;top:765px;width:245px;height:1px;background:#e2e2e2}
.social-dot{top:777px;width:22px;height:22px;border-radius:50%;background:linear-gradient(180deg,#9a9a9a,#6c6c6c)}

.foot-badge{left:220px;top:897px;width:46px;height:46px;border-radius:50%;background:#e4e4e4;border:2px solid var(--white);box-shadow:0 1px 3px rgba(0,0,0,.3);display:flex;align-items:center;justify-content:center;text-align:center}
.foot-badge span{font-family:"Arimo",sans-serif;font-weight:700;font-size:6.5px;line-height:1.1;color:#8a8a8a;width:34px}
.foot-rule{left:287px;top:919px;width:672px;height:1px;background:#e3e3e3}
.foot-links{left:286px;top:938px;font-size:7.5px;color:#999;display:flex;gap:9px}
.foot-copy{left:759px;top:938px;width:200px;text-align:right;font-size:7.5px;color:#999}
</style>
</head>
<body>
<div class="abs band-top"></div>
<div class="abs band-hero"></div>
<div class="abs band-foot"></div>

<div class="abs nav-bar"></div>
<div class="abs brand-badge"><span>Zippa Loop Trike</span></div>

<a class="abs order-btn">ORDER NOW</a>

<span class="abs nav-link is-active" style="left:422px">HOME</span>
<span class="abs nav-sep" style="left:485px"></span>
<span class="abs nav-link" style="left:510px">PRODUCT</span>
<span class="abs nav-sep" style="left:597px"></span>
<span class="abs nav-link" style="left:613px">HOME</span>
<span class="abs nav-sep" style="left:675px"></span>
<span class="abs nav-link" style="left:702px">CONTACT</span>
<span class="abs nav-sep" style="left:789px"></span>

<div class="abs cart-title">YOUR CART</div>
<div class="abs cart-count">
  <svg width="30" height="22" viewBox="0 0 30 22"><path d="M1 3h5l4 12h14l3-9H8" fill="none" stroke="#222" stroke-width="2.4" stroke-linejoin="round"/><circle cx="12" cy="19" r="2.2" fill="#222"/><circle cx="22" cy="19" r="2.2" fill="#222"/></svg>
  <span>5 items</span>
</div>

<h1 class="abs hero-title">ZIPPA LOOP TRIKE</h1>
<p class="abs hero-copy">Lorem Ipsum is simply dummy text of the printing and typesetting industry. Lorem Ipsum has been the industry's standard dummy text ever since the 1500</p>
<a class="abs buy-btn">
  <svg width="22" height="16" viewBox="0 0 30 22"><path d="M1 3h5l4 12h14l3-9H8" fill="none" stroke="#222" stroke-width="2.6" stroke-linejoin="round"/><circle cx="12" cy="19" r="2.4" fill="#222"/><circle cx="22" cy="19" r="2.4" fill="#222"/></svg>
  BUY NOW
</a>
<div class="abs hero-photo" role="img" aria-label="Silver ride-on toy bike with red wheels on a park path among trees"></div>

<div class="abs content-card"></div>

<h2 class="abs section-title is-red" style="left:244px;top:551px">WELCOME TO OUR WEBSITE</h2>
<p class="abs body-copy" style="left:244px;top:592px;width:445px">Lorem Ipsum is simply dummy text of the printing and typesetting industry. Lorem Ipsum has been the industry's standard dummy text ever since the 1500s, when an unknown printer took a galley of type and scrambled it to make a type specimen book.</p>
<div class="abs feature-thumb" role="img" aria-label="Blue ride-on toy bike on a park path"></div>
<p class="abs body-copy" style="left:387px;top:655px;width:302px">Lorem Ipsum is simply dummy text of the printing and typesetting industry. Lorem Ipsum has been the industry's standard dummy text ever since the 1500s, when an unknown printer took a galley of type and scrambled it to make a type specimen book.</p>
<p class="abs body-copy" style="left:244px;top:786px;width:445px">Lorem Ipsum is simply dummy text of the printing and typesetting industry. Lorem Ipsum has been the industry's standard dummy text ever since the 1500s, when an unknown printer took a galley of type and scrambled it to make a type specimen book.</p>

<div class="abs card-divider"></div>

<h2 class="abs section-title is-grey" style="left:718px;top:551px">SIGN UP FOR DISCOUNT</h2>
<div class="abs signup-field">email@example.com</div>
<div class="abs signup-btn">
  <svg width="24" height="18" viewBox="0 0 24 18"><rect x="1" y="3" width="22" height="14" fill="none" stroke="#fff" stroke-width="1.6"/><path d="M1 3l11 8 11-8" fill="none" stroke="#fff" stroke-width="1.6"/></svg>
</div>
<p class="abs body-copy" style="left:718px;top:634px;width:220px;font-size:8px;line-height:10px;color:#999">Lorem Ipsum is simply dummy text of the printing and typesetting industry</p>

<h2 class="abs section-title is-grey" style="left:718px;top:673px">LIKE ZIPPA LOOP TRIKE</h2>
<div class="abs share-row">
  <span class="share-btn"><i></i>Like</span><span class="share-count">3k</span>
  <span class="share-btn"><i></i>Chirp</span><span class="share-count">316</span>
  <span class="share-btn"><i></i>+1</span><span class="share-count">56</span>
  <span class="share-btn is-hot"><i></i>Share</span><span class="share-count">4.6K</span>
</div>

<h2 class="abs section-title is-grey" style="left:718px;top:743px">FOLLOW US ZIPPA LOOP TRIKE</h2>
<div class="abs follow-rule"></div>
<span class="abs social-dot" style="left:718px" aria-label="Friendly"></span>
<span class="abs social-dot" style="left:747px" aria-label="Chirpline"></span>
<span class="abs social-dot" style="left:776px" aria-label="Workbridge"></span>
<span class="abs social-dot" style="left:804px" aria-label="Reelbox"></span>

<div class="abs foot-badge"><span>Zippa Loop Trike</span></div>
<div class="abs foot-rule"></div>
<nav class="abs foot-links"><span>Home</span><span>|</span><span>About Us</span><span>|</span><span>Privacy Policy</span><span>|</span><span>Terms</span></nav>
<div class="abs foot-copy">2013. ZIPPA LOOP TRIKE. All right reserved</div>
</body>
</html>
```